VestoraHub.eu - need to polish our homepage (layout only)

We run a website project (http://cz.VestoraHub.eu) enabling free company formations via the Internet.

We now do complete redesign of the website which is almost ready but we still cannot get to proper shape of the homepage and we kindly ask you to participate on finalisation of this.

What we have now:
- design of sub-pages (see attached as NewSubPage design)

What must be preserved on homepage:
- upper horizontal menu and everything above it (logo, sign in button etc.)
- bottom quick navigation menu

What we would like to have (see attached HPSketch):
- unlike current homepage (http://cz.VestoraHub.eu) some introductory section just below the upper horizontal menu which will contain catching words/references

- more detailed website description and left navigation below this introductory section

- right banners stating amount of statutory fees and costs for registered office (if one chooses so)

- section for news

Thank you in advance for your proposals. In case of any queries please let us know.
Updates

Hello designers,

Many thanks for your first proposals, just.two general comments before I comment on particular designs:

1) We will probably want that the website does NOT include images of people but rather keep it as purely informative. The reason is that as we provide free service users often take us as sort of governmental agency and for such it is not very common here to have such type of public images on the website.

2) We will have 2 banners positions for our partners, one 970x200 leaderboard on the top of webpage and one left square below left navigation. You do not need to include them in your proposals, I am just mentioning this that this space must be left free for this purpose.

Many thanks for your effort so far, I will also comment separately on your particular designs.

Lukas

Requirements
Nice to have
• - you may consider substituting bullets in short catching sentences in introductory section by some icons expressing nature of the sentence

```html
<!DOCTYPE html>
<html lang="en">
<head>
<meta charset="utf-8">
<title>VestoraHub.eu – Free Company Formations Online</title>
<link href="https://fonts.googleapis.com/css2?family=Roboto:ital,wght@0,400;0,500;0,700;1,500&display=swap" rel="stylesheet">
<style>
:root{
  --blue:#0a4f95;
  --blue-dark:#063a70;
  --blue-bar:#3c79b4;
  --ink:#222;
  --muted:#666;
  --panel:#f2f2f2;
  --line:#d9d9d9;
  --light-blue:#eef5fd;
  --green:#3aa52f;
  --footer:#7f7f7f;
  --footer-dark:#2b2b2b;
}
*{box-sizing:border-box;margin:0;padding:0}
html,body{width:774px;height:1200px;overflow:hidden;background:#fff}
body{font-family:"Roboto",Arial,sans-serif;color:var(--ink);position:relative}
.abs{position:absolute}
.leaderboard{left:79px;top:10px;width:615px;height:62px;background:linear-gradient(90deg,#2a1a10,#4a3323 50%,#2a1a10)}
.brand{left:79px;top:92px;font-size:25px;font-weight:700;color:var(--blue);letter-spacing:-.3px;display:flex;align-items:center;gap:8px}
.brand .mark{width:16px;height:16px;background:var(--blue)}
.contact{left:398px;top:92px;font-size:9px;color:#888;line-height:14px}
.contact div{display:flex;align-items:center;gap:6px}
.auth{left:564px;top:96px;display:flex;gap:3px}
.btn{font-size:9px;color:#fff;padding:0 14px;height:19px;line-height:19px;border-radius:2px}
.btn.sign{background:var(--blue);width:59px;text-align:center;padding:0}
.btn.new{background:#999;width:69px;text-align:center;padding:0}
.mainnav{left:79px;top:136px;width:615px;height:35px;background:linear-gradient(#1d66b0,var(--blue-dark));display:flex;align-items:center}
.mainnav .home{width:40px;height:100%;display:flex;align-items:center;justify-content:center;border-right:1px solid #2d74bd}
.mainnav a{color:#fff;text-decoration:none;font-size:12px;padding:0 16px;height:100%;line-height:35px;border-right:1px solid #2d74bd}
.mainnav .tools{margin-left:auto;display:flex;gap:9px;padding-right:10px;align-items:center}
.intro{left:79px;top:189px;width:416px;height:152px;background:var(--panel);border:1px solid var(--line);padding:12px 15px}
.intro h1{font-size:17px;font-weight:400;color:var(--blue);letter-spacing:.3px}
.intro ul{list-style:none;margin-top:6px}
.intro li{font-size:11px;color:#666;height:18px;display:flex;align-items:center;gap:6px;padding-left:2px}
.intro .ctas{display:flex;gap:6px;margin-top:7px;padding-left:2px}
.intro .cta{background:var(--blue);color:#fff;font-size:8.5px;font-weight:700;height:23px;line-height:23px;padding:0 15px;border-radius:2px}
.side-box{background:var(--panel);border:1px solid var(--line)}
.counter{left:511px;top:189px;width:183px;height:67px;padding:8px 9px}
.counter .t{font-size:13px;color:#888}
.counter .n{display:flex;align-items:center;margin-top:4px;color:var(--blue)}
.counter .n b{font-size:21px}
.counter .n span{font-size:14px;margin-left:5px}
.counter .tag{margin-left:8px;background:var(--green);color:#fff;font-size:8px;font-weight:700;padding:3px 9px}
.testi{left:511px;top:262px;width:183px;height:79px;padding:8px 11px}
.testi .t{font-size:13px;color:#888}
.testi .badges{display:flex;gap:24px;margin-top:6px;padding-left:10px}
.testi .badge{width:38px;height:38px;border-radius:50%;background:#d8dfe8}
.leftnav{left:79px;top:360px;width:149px}
.leftnav div{height:24px;margin-bottom:2px;background:#e4e4e4;border:1px solid #c8c8c8;font-size:9.5px;font-weight:700;text-align:center;line-height:22px;color:#333;letter-spacing:.4px}
.leftnav div.active{background:var(--light-blue);border-color:var(--light-blue);color:var(--blue)}
.partner{left:79px;top:555px;width:142px;height:131px;background:linear-gradient(#0f2844,#0b1a2c);display:flex;align-items:center;justify-content:center}
.partner .name{background:#cce9f7;width:112px;height:53px;color:var(--blue);font-weight:700;font-size:14px;display:flex;align-items:center;justify-content:center}
.why{left:228px;top:360px;width:267px;height:422px;background:var(--light-blue);border:1px solid #c9ddf2;border-left:none;padding:10px 16px 0 20px}
.why h2{font-size:15px;color:#777;font-weight:700;margin-bottom:12px}
.why p{font-size:8.6px;line-height:12.8px;color:#444;margin-bottom:12px}
.why p::before{content:"›";color:var(--blue);font-weight:700;font-size:12px;margin-right:3px}
.costs{left:511px;top:360px;width:183px;height:93px;padding:6px 5px}
.office{left:511px;top:460px;width:183px;height:92px;padding:6px 5px}
.side-title{font-size:11.5px;color:var(--blue);letter-spacing:.4px;line-height:15px;padding:0 5px 4px}
.bar{background:var(--blue-bar);color:#fff;font-size:10px;height:20px;line-height:20px;padding:0 5px;margin-bottom:3px;display:flex;justify-content:space-between}
.bar b{font-size:11.5px}
.adjust{left:511px;top:560px;width:183px;height:83px;color:var(--blue);font-style:italic;font-weight:500;font-size:12.5px;text-align:center;line-height:18px;padding-top:14px;letter-spacing:.5px}
.news-title{left:79px;top:798px;width:615px;display:flex;align-items:flex-end;gap:6px}
.news-title h2{font-size:18px;font-weight:400;color:var(--blue);letter-spacing:.5px}
.news-title hr{flex:1;border:none;border-top:1px solid #ddd;margin-bottom:6px}
.news{top:833px;width:178px}
.news h3{font-size:10.5px;font-weight:700;margin-bottom:8px}
.news .card{height:84px;border:1px solid #e4e4e4;box-shadow:0 1px 3px rgba(0,0,0,.08);font-size:8.6px;line-height:12.8px;color:#444;text-align:center;padding:12px 10px}
.news .meta{display:flex;justify-content:flex-end;align-items:center;gap:12px;margin-top:8px;font-size:7.5px;text-align:center;letter-spacing:.5px;color:#333}
.news .avatar{width:38px;height:34px;background:#b9b1a7;border:2px solid #fff;box-shadow:0 0 2px #999}
.more{left:616px;top:1012px;font-size:10.5px;font-weight:700;color:var(--blue);text-decoration:underline}
.footer{left:0;top:1050px;width:774px;height:128px;background:var(--footer);color:#fff}
.fcol{position:absolute;top:31px;font-size:9px;line-height:12.8px}
.fcol h4{font-size:12.5px;font-weight:400;margin-bottom:8px}
.fcol div::before{content:"›";margin-right:6px}
.fsep{position:absolute;top:22px;width:1px;height:82px;background:#939393}
.copy{left:0;top:1178px;width:774px;height:22px;background:var(--footer-dark);color:#eee;font-size:7.5px;line-height:22px;padding-left:79px;letter-spacing:.3px}
</style>
</head>
<body>
<div class="abs leaderboard" role="img" aria-label="Partner leaderboard banner"></div>

<div class="abs brand"><span class="mark"></span>VestoraHub.eu</div>
<div class="abs contact">
  <div><svg width="9" height="9" viewBox="0 0 10 10"><path d="M2 1l2 2-1 1.5c.7 1.3 1.2 1.8 2.5 2.5L7 6l2 2-1.3 1.5C4.5 9 1 5.5.5 2.3z" fill="#999"/></svg>224 555 018</div>
  <div><svg width="9" height="7" viewBox="0 0 10 7"><rect width="10" height="7" fill="#999"/><path d="M0 0l5 4 5-4" stroke="#fff" fill="none"/></svg>info@vestorahub.eu</div>
</div>
<div class="abs auth"><div class="btn sign">Sign in</div><div class="btn new">New user</div></div>

<nav class="abs mainnav">
  <div class="home"><svg width="17" height="15" viewBox="0 0 17 15"><path d="M8.5 0L0 7.5h2.5V15h4.5v-5h3v5h4.5V7.5H17z" fill="#fff"/></svg></div>
  <a>Zalozeni S.R.O.</a><a>Zivnostensky list</a><a>Zalozeni A.S</a>
  <div class="tools">
    <svg width="15" height="15" viewBox="0 0 16 16"><circle cx="8" cy="8" r="5" fill="none" stroke="#fff" stroke-width="3" stroke-dasharray="2.5 1.4"/><circle cx="8" cy="8" r="3.5" fill="none" stroke="#fff" stroke-width="2"/></svg>
    <svg width="15" height="15" viewBox="0 0 16 16"><circle cx="8" cy="8" r="8" fill="#fff"/><text x="8" y="12.5" text-anchor="middle" font-size="12" font-weight="700" fill="#0a4f95" font-family="Arial">?</text></svg>
    <svg width="20" height="13" viewBox="0 0 20 13"><rect width="20" height="13" fill="#1f3f8a"/><path d="M0 0L20 13M20 0L0 13" stroke="#fff" stroke-width="2.5"/><path d="M0 0L20 13M20 0L0 13" stroke="#c8102e" stroke-width="1"/><path d="M10 0v13M0 6.5h20" stroke="#fff" stroke-width="4"/><path d="M10 0v13M0 6.5h20" stroke="#c8102e" stroke-width="2"/></svg>
  </div>
</nav>

<section class="abs intro">
  <h1>FREE COMPANY FORMATIONS ONLINE</h1>
  <ul>
    <li><svg width="11" height="11" viewBox="0 0 12 12"><rect x=".5" y="2.5" width="9" height="9" fill="none" stroke="#0a4f95"/><path d="M2.5 6l2.5 2.5L11.5.5" stroke="#0a4f95" stroke-width="2" fill="none"/></svg>Pay statutory registration fees only.</li>
    <li><svg width="11" height="11" viewBox="0 0 12 12"><rect x=".5" y="2.5" width="9" height="9" fill="none" stroke="#0a4f95"/><path d="M2.5 6l2.5 2.5L11.5.5" stroke="#0a4f95" stroke-width="2" fill="none"/></svg>Simply without attending state authorities.</li>
    <li><svg width="11" height="11" viewBox="0 0 12 12"><rect x=".5" y="2.5" width="9" height="9" fill="none" stroke="#0a4f95"/><path d="M2.5 6l2.5 2.5L11.5.5" stroke="#0a4f95" stroke-width="2" fill="none"/></svg>Registered capital from CZK 1.</li>
    <li><svg width="11" height="11" viewBox="0 0 12 12"><rect x=".5" y="2.5" width="9" height="9" fill="none" stroke="#0a4f95"/><path d="M2.5 6l2.5 2.5L11.5.5" stroke="#0a4f95" stroke-width="2" fill="none"/></svg>Company formed in 3-5 days.</li>
  </ul>
  <div class="ctas"><div class="cta">TRY UNBINDING REGISTRATION</div><div class="cta">HOW IT WORKS</div></div>
</section>

<div class="abs side-box counter">
  <div class="t">Registered up to Date</div>
  <div class="n"><b>4345</b><span>firms</span><span class="tag">REGISTRED</span></div>
</div>
<div class="abs side-box testi">
  <div class="t">Testimonails</div>
  <div class="badges"><div class="badge"></div><div class="badge"></div></div>
</div>

<nav class="abs leftnav">
  <div class="active">HOME</div><div>HOW IT WORKS</div><div>BEFORE BEGINNING</div><div>FORM COMPANY</div><div>CHECK REGISTRATION</div><div>FAQ</div><div>CONTACTS</div>
</nav>
<div class="abs partner"><div class="name">Banka Nova</div></div>

<section class="abs why">
  <h2>Why VestoraHub.eu?</h2>
  <p>The only system in the Czech Republic nabling the complex formation of new companies online through the Internet, without complicated dministration and running around state authorities.</p>
  <p>Free of charge handling with the payment of statutory registration fees only. Save 60-80% of costs in comparison with the formation of companies through a law firm or the purchase of a ready-made (shelf) company.</p>
  <p>Short registration process, all documentation is generated automatically online and the registration is completed in short periods (usually 3- 5 business days).</p>
  <p>Simple and user-friendly online registration form enabling tailor-made company formation for each user.</p>
  <p>Free-of-charge online formation of limited liability company (s.r.o.), trade license (ZL) and joint-stock company (a.s.). Possibility of another company forms through individual formation process.</p>
  <p>Professional legal support during the whole course of the company registration and 100% guarantee of registration in the Company Register.</p>
</section>

<div class="abs side-box costs">
  <div class="side-title">STATUTORY COSTS ONLY,<br>NO COMMITMENTS</div>
  <div class="bar"><span>S.R.O. formation from CZK</span><b>13,500</b></div>
  <div class="bar"><span>ŽL &nbsp;&nbsp;&nbsp;&nbsp;&nbsp;&nbsp;&nbsp;formation from CZK</span><b>1,000</b></div>
</div>
<div class="abs side-box office">
  <div class="side-title">NEED ALSO REGISTERED<br>OFFICE?</div>
  <div class="bar"><span>Prague from CZK <b>216/month</b></span></div>
  <div class="bar"><span>Ostrava from CZK <b>436/month</b></span></div>
</div>
<div class="abs side-box adjust">ADJUST YOUR COMPANY<br>DOCUMENTATION TO<br>2014 LEGISLATION</div>

<div class="abs news-title"><h2>NEWS</h2><hr></div>
<article class="abs news" style="left:80px">
  <h3>Applies to The Startups of.........</h3>
  <div class="card">Startups of the Year 2011 is a new competition, designated for starting entrepreneurs where valuable prices and professional support may be found for the start of business. The competition was</div>
  <div class="meta"><div>30. 09. 2011<br>Martin Kolar</div><div class="avatar" role="img" aria-label="Author portrait"></div></div>
</article>
<article class="abs news" style="left:298px">
  <h3>The change of court fees...........</h3>
  <div class="card">As of 1.9.2011, the change to statutory court fees will become effective for the registration of new companies into the Czech Company Register .<br>Instead of the current CZK 5,000</div>
  <div class="meta"><div>15. 08. 2011<br>Jan</div><div class="avatar" role="img" aria-label="Author portrait"></div></div>
</article>
<article class="abs news" style="left:517px">
  <h3>Applies to The Startups of.........</h3>
  <div class="card">Startups of the Year 2011 is a new competition, designated for starting entrepreneurs where valuable prices and professional support may be found for the start of business. The competition was</div>
  <div class="meta"><div>30. 09. 2011<br>Eva</div><div class="avatar" role="img" aria-label="Author portrait"></div></div>
</article>
<div class="abs more">More News.......</div>

<footer class="abs footer">
  <div class="fcol" style="left:79px;top:34px"><h4>Form Company</h4><div>S.R.O</div><div>Trade License</div></div>
  <div class="fsep" style="left:213px"></div>
  <div class="fcol" style="left:251px"><h4>Clint Zone</h4><div>My Registrations</div><div>Check Registration</div><div>My Profile</div></div>
  <div class="fsep" style="left:381px"></div>
  <div class="fcol" style="left:413px;top:33px"><h4>VestoraHub.eu</h4><div>How it Works</div><div>Before Beginnings</div><div>Business Conditions</div><div>Affilate Program</div></div>
  <div class="fsep" style="left:565px"></div>
  <div class="fcol" style="left:607px;top:33px"><h4>Support</h4><div>Contact</div><div>FAQ</div></div>
</footer>
<div class="abs copy">Copyright © 2014 VestoraHub.eu, all rights reserved</div>
</body>
</html>
```